Business Card Design for new logo

Business card Design for new logo. Follow colors from logo.
The company has offices in multiple comtries
Want to have some bulltes on the countries and also on the main services

Something like
USA*Dominican Republic*LATAM

Consulting*Healthcare IT*Tranformation

Industry/Entity Type

Information Technology

Contact Information for Business Card

Address, Phones, countries, name and position

Lucan morrel

Founder and CEO

947 Tarrow Ln
Halden vale, ST 00412

Lmorrel@quendoxcare.com

www.quendoxcare.com

555-304-6182

555-222-2222

```html
<!DOCTYPE html>
<html lang="en">
<head>
<meta charset="UTF-8">
<title>Quendox Care — Business Card</title>
<link href="https://fonts.googleapis.com/css2?family=Roboto:wght@400;500;700&display=swap" rel="stylesheet">
<style>
  :root {
    --stage: #e4e4e4;
    --brand-blue: #2474b8;
    --brand-orange: #f28c44;
    --paper: #ffffff;
    --ink-light: #ffffff;
  }
  * { margin: 0; padding: 0; box-sizing: border-box; }
  html, body { width: 1200px; height: 900px; overflow: hidden; }
  body {
    background: var(--stage);
    font-family: "Roboto", Arial, sans-serif;
    position: relative;
  }
  .card {
    position: absolute;
    top: 295px;
    width: 540px;
    height: 310px;
    border-radius: 26px;
    background: var(--brand-blue);
    overflow: hidden;
    box-shadow: 0 14px 30px rgba(0,0,0,0.18);
    color: var(--ink-light);
  }
  .card--front { left: 40px; }
  .card--back { left: 620px; }

  /* front */
  .brand-lockup {
    position: absolute;
    top: 58px; left: 0; right: 0;
    display: flex; align-items: center; justify-content: center; gap: 12px;
  }
  .brand-dot {
    width: 22px; height: 22px; border-radius: 50%;
    background: var(--brand-orange);
  }
  .brand-name {
    font-size: 30px; font-weight: 500; color: var(--ink-light);
  }
  .bullet-list { position: absolute; list-style: none; }
  .bullet-list li { position: relative; padding-left: 12px; }
  .bullet-list li::before {
    content: ""; position: absolute; left: 0; top: 50%;
    width: 5px; height: 5px; margin-top: -3px; border-radius: 50%;
    background: var(--brand-orange);
  }
  .bullet-list--countries { left: 58px; top: 168px; font-size: 14px; line-height: 27px; }
  .bullet-list--services { left: 320px; top: 176px; font-size: 16px; line-height: 33px; }

  /* back */
  .back-art { position: absolute; inset: 0; width: 100%; height: 100%; }
  .holder { position: absolute; left: 36px; top: 58px; }
  .holder-name { font-size: 19px; font-weight: 700; color: var(--brand-orange); }
  .holder-title { font-size: 14px; margin-top: 4px; }
  .contact-list { position: absolute; left: 36px; top: 145px; list-style: none; font-size: 15px; }
  .contact-item { display: flex; align-items: flex-start; gap: 10px; margin-bottom: 7px; line-height: 19px; }
  .contact-icon { width: 19px; height: 19px; flex: none; }
  .back-brand {
    position: absolute; right: 30px; top: 168px;
    font-size: 30px; font-weight: 500; color: var(--brand-blue);
  }
</style>
</head>
<body>

  <section class="card card--front" aria-label="Card front">
    <div class="brand-lockup">
      <span class="brand-dot"></span>
      <span class="brand-name">Quendox Care</span>
    </div>
    <ul class="bullet-list bullet-list--countries">
      <li>USA</li>
      <li>Dominican Republic</li>
      <li>LATAM</li>
    </ul>
    <ul class="bullet-list bullet-list--services">
      <li>Consulting</li>
      <li>Healthcare IT</li>
      <li>Tranformation</li>
    </ul>
  </section>

  <section class="card card--back" aria-label="Card back">
    <svg class="back-art" viewBox="0 0 540 310" preserveAspectRatio="none" aria-hidden="true">
      <path d="M300 120 C272 190 250 250 262 310 L290 310 C272 250 288 190 312 130 Z" fill="var(--brand-orange)"/>
      <path d="M318 0 C292 55 306 115 292 175 C280 230 268 275 282 310 L540 310 L540 0 Z" fill="var(--paper)"/>
    </svg>

    <div class="holder">
      <div class="holder-name">Lucan morrel</div>
      <div class="holder-title">Founder and CEO</div>
    </div>

    <ul class="contact-list">
      <li class="contact-item">
        <svg class="contact-icon" viewBox="0 0 20 20" aria-hidden="true"><circle cx="10" cy="10" r="10" fill="var(--brand-orange)"/><path d="M6 5 L8 5 L9 8 L7.8 9 Q9 11.5 11 12.2 L12 11 L15 12 L15 14 Q14 15.5 12 15 Q6.5 13 5 8 Q4.8 6 6 5Z" fill="#fff"/></svg>
        <span>555-304-6182</span>
      </li>
      <li class="contact-item">
        <svg class="contact-icon" viewBox="0 0 20 20" aria-hidden="true"><circle cx="10" cy="10" r="10" fill="var(--brand-orange)"/><rect x="7" y="4.5" width="6" height="11" rx="1" fill="none" stroke="#fff" stroke-width="1.4"/><circle cx="10" cy="13.5" r="0.8" fill="#fff"/></svg>
        <span>555-222-2222</span>
      </li>
      <li class="contact-item">
        <svg class="contact-icon" viewBox="0 0 20 20" aria-hidden="true"><circle cx="10" cy="10" r="10" fill="var(--brand-orange)"/><rect x="5" y="6.5" width="10" height="7" fill="#fff"/><path d="M5 6.5 L10 10.5 L15 6.5" fill="none" stroke="var(--brand-orange)" stroke-width="1.1"/></svg>
        <span>Lmorrel@quendoxcare.com</span>
      </li>
      <li class="contact-item">
        <svg class="contact-icon" viewBox="0 0 20 20" aria-hidden="true"><circle cx="10" cy="10" r="10" fill="var(--brand-orange)"/><g fill="none" stroke="#fff" stroke-width="1.1"><circle cx="10" cy="10" r="5"/><ellipse cx="10" cy="10" rx="2.2" ry="5"/><line x1="5" y1="10" x2="15" y2="10"/></g></svg>
        <span>www.quendoxcare.com</span>
      </li>
      <li class="contact-item">
        <svg class="contact-icon" viewBox="0 0 20 20" aria-hidden="true"><circle cx="10" cy="10" r="10" fill="var(--brand-orange)"/><path d="M10 16 Q5.5 10.5 5.5 8.5 A4.5 4.5 0 0 1 14.5 8.5 Q14.5 10.5 10 16Z" fill="#fff"/><circle cx="10" cy="8.5" r="1.7" fill="var(--brand-orange)"/></svg>
        <span>947 Tarrow Ln<br>Halden vale, ST 00412</span>
      </li>
    </ul>

    <div class="back-brand">Quendox Care</div>
  </section>

</body>
</html>
```